Out of town New Masters of Accounting

size of ad is 7” x 9.6”
please leave one inch on bottom for footer
We want to attract out of town students to join this master's in accounting program.
You DO NOT  have to use a picture of a person.
But if you do, it should be a  male with a white shirt and should not have long hair.(look like a young executive)
THE TEXT OF THE AD IS IN THE ATTACHMENTS
THE CAP LETTERS ARE THE INSTRUCTIONS

The age we are trying to attract is from 20-30 of ages.
- a clear ad .. the text should not take up the entire ad.. it should not be very crowded -
it should be an attractive ad that people would want to see and stand out
- the text very big and take up the entire ad

```html
<!DOCTYPE html>
<html lang="en">
<head>
<meta charset="utf-8">
<title>Remote Masters in Accounting – Flyer Options</title>
<link href="https://fonts.googleapis.com/css2?family=Roboto:wght@400;500;700;900&display=swap" rel="stylesheet">
<style>
  :root {
    --page-bg: #ffffff;
    --card-bg: #ffffff;
    --ink: #1e2139;
    --accent: #f5a000;
    --accent-wash: #fdf1d6;
    --dot-field: #f4f4f7;
    --badge-fill: #f39a12;
  }
  * { box-sizing: border-box; margin: 0; padding: 0; }
  html, body { width: 1200px; height: 1000px; overflow: hidden; background: var(--page-bg); }
  body { position: relative; font-family: "Roboto", Arial, sans-serif; color: var(--ink); }

  .flyer {
    position: absolute; top: 140px; width: 525px; height: 720px;
    background: var(--card-bg); overflow: hidden;
    box-shadow: 0 6px 18px rgba(0,0,0,0.22);
  }
  .flyer--decorated { left: 56px; }
  .flyer--plain { left: 621px; }

  .flyer__decor { position: absolute; inset: 0; }

  .ranking-tab {
    position: absolute; left: 209px; top: 0; width: 107px; height: 166px;
    filter: drop-shadow(0 1px 2px rgba(0,0,0,0.18));
  }

  .flyer__content {
    position: absolute; left: 0; right: 0; top: 179px;
    text-align: center;
  }
  .headline {
    font-weight: 900; font-size: 27.5px; line-height: 32.5px;
    letter-spacing: 0.2px; color: var(--ink);
  }
  .launch-date {
    margin-top: 15px; font-weight: 700; font-size: 16.5px; line-height: 16px;
    color: var(--accent);
  }
  .launch-note { font-size: 13px; line-height: 14px; }
  .divider {
    margin: 18px auto 0; width: 90px; font-size: 10px; line-height: 8px;
    letter-spacing: 0; font-weight: 500; color: var(--ink);
  }
  .pitch { margin-top: 17px; font-size: 12.5px; line-height: 15px; }
  .section-title {
    margin-top: 23px; font-weight: 700; font-size: 11.5px; line-height: 13px;
    color: var(--accent);
  }
  .section-body { font-size: 12.5px; line-height: 15px; }
  .section-title--after-divider { margin-top: 25px; }
  .closing { margin-top: 34px; font-size: 12.5px; line-height: 15px; }
</style>
</head>
<body>

<article class="flyer flyer--decorated">
  <svg class="flyer__decor" width="525" height="720" viewBox="0 0 525 720">
    <rect x="4" y="20" width="106" height="145" fill="var(--dot-field)" role="img" aria-label="Decorative dot pattern area"/>
    <rect x="455" y="20" width="70" height="130" fill="var(--accent-wash)" role="img" aria-label="Decorative striped shape area"/>
    <rect x="320" y="136" width="88" height="26" fill="var(--accent-wash)" role="img" aria-label="Decorative wave pattern area"/>
    <rect x="0" y="355" width="26" height="80" fill="var(--accent-wash)" role="img" aria-label="Decorative ring shape area"/>
    <rect x="394" y="465" width="125" height="130" fill="var(--dot-field)" role="img" aria-label="Decorative dot pattern area"/>
    <rect x="42" y="582" width="88" height="28" fill="var(--accent-wash)" role="img" aria-label="Decorative wave pattern area"/>
    <rect x="255" y="686" width="40" height="34" fill="var(--accent-wash)" role="img" aria-label="Decorative cross shape area"/>
  </svg>

  <svg class="ranking-tab" viewBox="0 0 107 166" role="img" aria-label="Ranking badge">
    <polygon points="0,0 107,0 107,130 53.5,166 0,130" fill="#fff" stroke="#e6e6e6" stroke-width="1"/>
    <circle cx="53.5" cy="62" r="28" fill="var(--badge-fill)"/>
  </svg>

  <div class="flyer__content">
    <h1 class="headline">ALL NEW!<br>REMOTE PROGRAM FOR<br>OUT OF TOWN STUDENTS</h1>
    <p class="launch-date">BEGINNING AUGUST 17</p>
    <p class="launch-note">New lower prices</p>
    <p class="divider">ooooooooooooo<br>ooooooooo</p>
    <p class="pitch">Advance further in your career with<br>a&nbsp; masters of science in accounting.</p>
    <p class="section-title">LAUVEL INDEX -- NORTHBROOK HOLLIS UNIVERSITY (NHU)</p>
    <p class="section-body">Master in Accounting Program Received the<br>highest possible star rating.</p>
    <p class="divider">ooooooooooooo<br>ooooooooo</p>
    <p class="section-title section-title--after-divider">TVL/BRIGHTWATER CAREER NETWORK PLACEMENT ADVANTAGE</p>
    <p class="section-body">*96% placement rate<br>*8 placement coordinators<br>* Decades of relationships with 100's of firm</p>
    <p class="closing">A masters in only 15 months.</p>
  </div>
</article>

<article class="flyer flyer--plain">
  <svg class="ranking-tab" viewBox="0 0 107 166" role="img" aria-label="Ranking badge">
    <polygon points="0,0 107,0 107,130 53.5,166 0,130" fill="#fff" stroke="#e6e6e6" stroke-width="1"/>
    <circle cx="53.5" cy="62" r="28" fill="var(--badge-fill)"/>
  </svg>

  <div class="flyer__content">
    <h1 class="headline">ALL NEW!<br>REMOTE PROGRAM FOR<br>OUT OF TOWN STUDENTS</h1>
    <p class="launch-date">BEGINNING AUGUST 17</p>
    <p class="launch-note">New lower prices</p>
    <p class="divider">ooooooooooooo<br>ooooooooo</p>
    <p class="pitch">Advance further in your career with<br>a&nbsp; masters of science in accounting.</p>
    <p class="section-title">LAUVEL INDEX -- NORTHBROOK HOLLIS UNIVERSITY (NHU)</p>
    <p class="section-body">Master in Accounting Program Received the<br>highest possible star rating.</p>
    <p class="divider">ooooooooooooo<br>ooooooooo</p>
    <p class="section-title section-title--after-divider">TVL/BRIGHTWATER CAREER NETWORK PLACEMENT ADVANTAGE</p>
    <p class="section-body">*96% placement rate<br>*8 placement coordinators<br>* Decades of relationships with 100's of firm</p>
    <p class="closing">A masters in only 15 months.</p>
  </div>
</article>

</body>
</html>
```